Business Cards for a company that provides webstore services to veterinarians

We need business cards designed for our main service PawCartHub. PawCartHub is a webstore that veterinarian clinics can use to that will allow their clients to purchase products for their pets. Our company is Brindlow Veterinary Solutions (BVS). Our mission statement is We love pets! We will do everything possible to facilitate along, healthy and happy relationship with their families.

Target Market(s)

Veterinarians

Industry/Entity Type

Veterinary

Contact Information for Business Card

I would like the design to incorporate the colours our our company. Cards should have room for employee name, title (only necessary in two instances), phone number, mobile number, email address and linkedin symbol and related profile name ie Marla Quinton. I would like the PawCartHub logo to appear on one side and BVS logo to appear on the other. I will need both an english and french version. I can provide the french translation. Please focus on english version and then we will translate

Colors

Designer to choose colors to be used in the design.

Requirements
Must have
• one side - PawCartHub logo with persons name, phone number, mobile number, email address
• second side - BVS logo
• colours should be consistent with our company. colours are as follows:
• Red
• RGB: 190 / 30 / 45
• CYMK: 14 / 100 / 90 /10
• Hex: #BE1E2D
• Gray
• RGB: 88 / 89 / 86
• CYMK: 3 / 2 / 0 /64
• Hex: #585956
Nice to have
• address of company - can be on either side address is 4817 Feldmoor Street Suite 305 Burlington ON K2R 6T4. Toll free number will vary depending on person
• Linkedin symbol and name of person
• on second side with BVS logo our company's mission statement
Should not have
• nothing comes to mind

```html
<!DOCTYPE html>
<html lang="en">
<head>
<meta charset="utf-8">
<title>PawCartHub Business Card</title>
<link rel="stylesheet" href="https://fonts.googleapis.com/css2?family=Open+Sans:wght@400;600;700&display=swap">
<style>
  :root {
    --brand-red: #be1e2d;
    --brand-gray: #585956;
    --card-back: #5a5a5c;
    --backdrop: #8c8c8c;
    --paper: #ffffff;
  }
  * { margin: 0; padding: 0; box-sizing: border-box; }
  html, body {
    width: 1200px;
    height: 1000px;
    overflow: hidden;
    background: var(--backdrop);
    font-family: "Open Sans", Arial, sans-serif;
  }
  .canvas { position: relative; width: 1200px; height: 1000px; }
  .card {
    position: absolute;
    left: 348px;
    width: 519px;
    height: 305px;
    overflow: hidden;
  }
  .card--front { top: 149px; background: var(--paper); }
  .card--back { top: 530px; background: var(--card-back); }
  .wave { position: absolute; inset: 0; }
  .brand-name {
    position: absolute;
    top: 64px;
    right: 44px;
    font-size: 26px;
    font-weight: 600;
    color: var(--brand-gray);
  }
  .contact-block {
    position: absolute;
    left: 30px;
    top: 168px;
    color: var(--paper);
  }
  .person-name { font-size: 17px; font-weight: 600; line-height: 22px; }
  .person-title { font-size: 12px; line-height: 15px; margin-bottom: 12px; }
  .contact-list { list-style: none; }
  .contact-list li {
    display: flex;
    align-items: center;
    gap: 7px;
    font-size: 12px;
    line-height: 16px;
  }
  .contact-list svg { width: 10px; height: 10px; fill: var(--paper); flex: none; }
  .company-lockup {
    position: absolute;
    left: 0;
    right: 0;
    top: 128px;
    text-align: center;
    color: var(--paper);
  }
  .company-name {
    font-size: 24px;
    font-weight: 600;
    line-height: 30px;
  }
  .company-tagline {
    margin-top: 8px;
    font-size: 11px;
    font-weight: 400;
    letter-spacing: 1.5px;
    text-transform: uppercase;
  }
</style>
</head>
<body>
<main class="canvas">
  <section class="card card--front">
    <svg class="wave" viewBox="0 0 519 305" width="519" height="305" aria-hidden="true">
      <path d="M222,150 C300,178 368,196 428,192 C468,189 498,168 519,143 L519,166 C498,186 468,202 428,205 C368,209 300,190 222,150 Z" fill="var(--brand-gray)"/>
      <path d="M0,145 C80,118 160,126 240,158 C310,186 380,206 438,203 C476,201 502,188 519,174 L519,305 L0,305 Z" fill="var(--brand-red)"/>
      <path d="M240,158 C310,186 380,206 438,203 C476,201 502,188 519,174" fill="none" stroke="var(--paper)" stroke-width="2.5"/>
    </svg>

    <div class="brand-name">PawCartHub</div>

    <div class="contact-block">
      <p class="person-name">Marla Quinton</p>
      <p class="person-title">President</p>
      <ul class="contact-list">
        <li>
          <svg viewBox="0 0 10 10"><path d="M2,0.5 L3.6,2.6 L2.8,3.6 C3.4,5 4.8,6.4 6.3,7.1 L7.3,6.3 L9.5,7.9 L8.4,9.5 C4.2,9 1,5.8 0.5,1.6 Z"/></svg>
          <span>555-0142-3380</span>
        </li>
        <li>
          <svg viewBox="0 0 10 10"><path d="M2.5,0 H7.5 V10 H2.5 Z M3.5,1 V8 H6.5 V1 Z"/></svg>
          <span>555-0197-6214</span>
        </li>
        <li>
          <svg viewBox="0 0 10 10"><path d="M0,2 H10 V8.5 H0 Z M0.8,2.6 L5,5.6 L9.2,2.6" stroke="var(--brand-red)" stroke-width="0.8"/></svg>
          <span>www.pawcarthub.com</span>
        </li>
        <li>
          <svg viewBox="0 0 10 10"><rect x="0" y="0" width="10" height="10" rx="1.5"/></svg>
          <span>/MarlaQuinton</span>
        </li>
      </ul>
    </div>
  </section>

  <section class="card card--back">
    <div class="company-lockup">
      <p class="company-name">Brindlow Veterinary Solutions</p>
      <p class="company-tagline">Caring for every paw</p>
    </div>
  </section>
</main>
</body>
</html>
```